Heritage Hollow Business Cards

Require a business card design. <br/><br/>Needs to include logo (either round or long version) plus these details:<br/>Maya Torvel<br/>Heritage Hollow<br/>maya@quonbrook.com.au<br/>02 6481 7390<br/>PO Box Glenwarra NSW 2913<br/>www.heritagehollow.com.au<br/><br/>I need in an editable format so that I can create for multiple staff members. <br/><br/>

Target Market(s)

We are an online store selling renovation products to home owners are builders. Looking for a classic classy design.

Industry/Entity Type

Home And Garden

Contact Information for Business Card

Maya Torvel
Heritage Hollow
maya@quonbrook.com.au
02 6481 7390
PO Box Glenwarra NSW 2913
www.heritagehollow.com.au

Colors

Designer to choose colors to be used in the design.

Requirements
Must have
• Must include Logo.

```html
<!DOCTYPE html>
<html lang="en">
<head>
<meta charset="utf-8">
<title>Heritage Hollow Business Cards</title>
<link rel="stylesheet" href="https://fonts.googleapis.com/css2?family=Open+Sans:wght@400;600&display=swap">
<style>
  :root {
    --backdrop: #ece6dc;
    --card: #ffffff;
    --ink: #333333;
    --sage-dark: #4f6e60;
    --sage-light: #829c8f;
    --slate: #5a5a5a;
    --social: #6a6a6a;
    --icon-grey: #d4d6d8;
  }
  * { box-sizing: border-box; margin: 0; padding: 0; }
  html, body {
    width: 1200px; height: 1200px; overflow: hidden;
    background: var(--backdrop);
    font-family: "Open Sans", sans-serif;
    color: var(--ink);
  }
  .card {
    position: absolute;
    left: 281px;
    width: 636px; height: 405px;
    background: var(--card);
    border-radius: 0 36px 0 36px;
    overflow: hidden;
  }
  .card--front { top: 175px; }
  .card--back { top: 620px; }
  .card__bands { position: absolute; left: 0; top: 0; width: 636px; height: 405px; }

  /* Front */
  .brand {
    position: absolute; left: 52px; top: 168px;
    display: flex; align-items: center; gap: 16px;
  }
  .brand__mark {
    width: 46px; height: 46px; flex: none;
    border: 2px solid var(--ink);
    border-radius: 50%;
  }
  .brand__name {
    font-size: 54px; font-weight: 400; line-height: 1;
    color: var(--ink); letter-spacing: 0.5px;
    white-space: nowrap;
  }
  .website {
    position: absolute; left: 349px; top: 371px;
    display: flex; align-items: center; gap: 10px;
    color: #fff; font-size: 16px;
  }
  .website svg { width: 28px; height: 28px; }

  /* Back */
  .contact-list { position: absolute; left: 66px; top: 90px; list-style: none; }
  .contact-list li {
    display: flex; align-items: center; gap: 24px;
    height: 34px; margin-bottom: 10px;
    font-size: 14.5px; color: var(--ink);
    white-space: nowrap;
  }
  .contact-list svg { width: 32px; height: 32px; flex: none; }
  .divider { position: absolute; width: 2px; background: var(--slate); }
  .divider--long { left: 323px; top: 87px; height: 113px; }
  .divider--short { left: 336px; top: 107px; height: 67px; }
  .person {
    position: absolute; right: 35px; top: 108px; text-align: right;
  }
  .person__name { font-size: 42px; font-weight: 400; line-height: 1.05; color: var(--ink); }
  .person__company { font-size: 19px; color: var(--sage-dark); margin-top: 2px; }
  .social {
    position: absolute; right: 39px; top: 267px;
    display: flex; gap: 10px;
  }
  .social span { width: 31px; height: 31px; background: var(--social); display: block; }
  .address {
    position: absolute; right: 35px; top: 306px;
    font-size: 14.5px; color: var(--ink); white-space: nowrap;
  }
</style>
</head>
<body>

<section class="card card--front" aria-label="Business card front">
  <svg class="card__bands" viewBox="0 0 636 405" aria-hidden="true">
    <polygon points="241,337 636,337 636,356 262,356" fill="var(--slate)"/>
    <polygon points="262,337 636,337 636,356 283,356" fill="var(--sage-light)"/>
    <rect x="0" y="356" width="636" height="49" fill="var(--sage-dark)"/>
  </svg>
  <div class="brand">
    <div class="brand__mark" aria-hidden="true"></div>
    <div class="brand__name">Heritage Hollow</div>
  </div>
  <div class="website">
    <svg viewBox="0 0 30 30" aria-hidden="true">
      <circle cx="15" cy="15" r="14" fill="#fff"/>
      <circle cx="15" cy="15" r="8" fill="none" stroke="var(--sage-dark)" stroke-width="2"/>
      <ellipse cx="15" cy="15" rx="3.5" ry="8" fill="none" stroke="var(--sage-dark)" stroke-width="1.5"/>
      <line x1="7" y1="15" x2="23" y2="15" stroke="var(--sage-dark)" stroke-width="1.5"/>
    </svg>
    <span>www.heritagehollow.com.au</span>
  </div>
</section>

<section class="card card--back" aria-label="Business card back">
  <svg class="card__bands" viewBox="0 0 636 405" aria-hidden="true">
    <polygon points="241,337 636,337 636,356 262,356" fill="var(--slate)"/>
    <polygon points="262,337 636,337 636,356 283,356" fill="var(--sage-light)"/>
    <rect x="0" y="356" width="636" height="49" fill="var(--sage-dark)"/>
  </svg>

  <ul class="contact-list">
    <li>
      <svg viewBox="0 0 34 34" aria-hidden="true">
        <rect x="1" y="1" width="32" height="32" rx="5" fill="var(--sage-dark)"/>
        <path d="M12 8 q-4 2 -2 9 q3 8 10 10 l3 -3 l-4 -4 l-2 2 q-4 -3 -5 -7 l2 -2 z" fill="#fff"/>
      </svg>
      <span>02 6481 7390</span>
    </li>
    <li>
      <svg viewBox="0 0 34 34" aria-hidden="true">
        <circle cx="17" cy="17" r="16" fill="var(--icon-grey)" stroke="#b9bcbf"/>
        <rect x="13" y="9" width="8" height="16" rx="1.5" fill="#555"/>
        <rect x="14.5" y="11" width="5" height="5" fill="#ddd"/>
      </svg>
      <span>0400.618.275</span>
    </li>
    <li>
      <svg viewBox="0 0 34 34" aria-hidden="true">
        <circle cx="17" cy="17" r="16" fill="var(--icon-grey)" stroke="#b9bcbf"/>
        <rect x="10" y="12" width="14" height="10" fill="none" stroke="#555" stroke-width="1.6"/>
        <polyline points="10,12 17,18 24,12" fill="none" stroke="#555" stroke-width="1.6"/>
      </svg>
      <span>maya@quonbrook.com.au</span>
    </li>
  </ul>

  <div class="divider divider--long"></div>
  <div class="divider divider--short"></div>

  <div class="person">
    <div class="person__name">Maya Torvel</div>
    <div class="person__company">Heritage Hollow</div>
  </div>

  <div class="social" aria-label="Social media links">
    <span></span><span></span><span></span><span></span>
  </div>

  <div class="address">Address: PO Box Glenwarra NSW 2913</div>
</section>

</body>
</html>
```